KVLO EXTRA PowerPoint

I need to convert our online business to a power point. A step by step presentation,
I want a POWER POINT to use one on one and as well as for a group.
Like to see moving parts to show value and savings. Very clear " dream Vacation" pictures. This is the future of vacationing!

web site:
KVLO.online

two videos below to be included
Updates

The first four days i never received anything. Their was a mixup regarding my power point.

Target Market(s)

dream vacations, for everyone

Number of Pages Required

5+ page

Font styles to use
Sans Serif

Colors

Designer to choose colors to be used in the design.

Requirements
Must have
• Look professional
• movement
Nice to have
• Easy to understand and use. show savings and value
• 10 to 20 pages min.
Should not have
• look nothing like my old power point

```html
<!DOCTYPE html>
<html lang="en">
<head>
<meta charset="utf-8">
<title>KVLO EXTRA Presentation</title>
<link href="https://fonts.googleapis.com/css2?family=Open+Sans:wght@400;600;700;800&display=swap" rel="stylesheet">
<style>
:root{
  --blue:#1a8fd6;
  --blue-deep:#0d6fb8;
  --sky:#2aa7e0;
  --orange:#f18a1f;
  --orange-deep:#e8701a;
  --ink:#1b1b1b;
  --navy:#1d3a5c;
  --paper:#f4f4f4;
  --grey:#8a8a8a;
  --stage-mid:#4a4a4a;
  --stage-edge:#262626;
}
*{margin:0;padding:0;box-sizing:border-box}
html,body{width:999px;height:1200px;overflow:hidden}
body{
  font-family:"Open Sans",Arial,sans-serif;
  background:radial-gradient(ellipse at center,var(--stage-mid) 0%,var(--stage-edge) 100%);
  position:relative;color:var(--ink);
}
.slide{position:absolute;background:linear-gradient(180deg,#fff 0%,var(--paper) 100%);overflow:hidden;box-shadow:0 0 6px rgba(0,0,0,.35)}
.s1{left:139px;top:57px;width:345px;height:259px}
.s2{left:507px;top:57px;width:346px;height:259px}
.s3{left:139px;top:337px;width:345px;height:259px}
.s4{left:507px;top:337px;width:346px;height:259px}
.s5{left:139px;top:613px;width:345px;height:258px}
.s6{left:507px;top:613px;width:346px;height:258px}
.s7{left:139px;top:889px;width:345px;height:259px}
.s8{left:507px;top:889px;width:346px;height:259px}

.header{position:absolute;left:0;top:0;width:100%;height:80px}
.header-brand{position:absolute;left:12px;top:12px;color:#fff;font-size:10px;font-weight:700;letter-spacing:.5px}
.header-url{position:absolute;right:34px;top:14px;color:#fff;font-size:7.5px;font-weight:700;letter-spacing:1.6px}

.photo{position:absolute}
.ring{border-radius:50%;border:4px solid var(--orange);box-shadow:0 1px 3px rgba(0,0,0,.25)}
.photo-pool{background:linear-gradient(180deg,#5cb4e8 0%,#9fd2ee 45%,#2f9bc9 70%,#6b7a4a 100%)}
.photo-hut{background:linear-gradient(180deg,#9ad4f2 0%,#49a6d6 55%,#1d7fb3 100%)}
.photo-couple{background:linear-gradient(180deg,#e8f2fa 0%,#d7b48a 60%,#f1efe9 100%)}
.photo-chairs{background:linear-gradient(180deg,#69b8ea 0%,#d9e9f3 50%,#e7d4ac 100%)}
.photo-palm{background:linear-gradient(180deg,#4fa9e6 0%,#8ccbee 50%,#e6d7b0 100%)}
.photo-map{background:linear-gradient(160deg,#c9d9c4 0%,#9ec5d6 45%,#d7b98c 100%)}

.title{position:absolute;color:var(--sky);font-weight:700}
.bullets{position:absolute;list-style:none}
.bullets li{position:relative;padding-left:18px;font-weight:600}
.bullets li::before{content:"";position:absolute;left:2px;top:.35em;border-left:5px solid var(--ink);border-top:3px solid transparent;border-bottom:3px solid transparent}
.bullets li::after{content:"";position:absolute;left:0;top:.35em;width:2px;height:6px;background:var(--ink)}
.url-foot{position:absolute;font-size:8px;letter-spacing:2px;color:var(--ink);font-weight:600}

/* cover */
.cover-name{position:absolute;left:28px;top:66px;font-size:21px;font-weight:700;color:var(--navy);display:flex;align-items:center;gap:7px}
.cover-name .dot{width:11px;height:11px;border-radius:50%;background:var(--orange)}
.cover-sky{position:absolute;left:0;top:0;width:100%;height:100%}
.s1 .bullets{left:20px;top:216px;font-size:8.3px}
.s1 .bullets li{font-weight:400;line-height:11px;padding-left:12px}
.s1 .bullets li::before{left:0}
.s1 .bullets li::after{display:none}

/* who */
.s2 .title{left:16px;top:68px;font-size:12.5px}
.s2 .bullets{left:16px;top:92px;font-size:7px}
.s2 .bullets li{line-height:9px;margin-bottom:9.6px}

/* rate */
.beach{left:0;top:0;width:100%;height:100%;background:linear-gradient(180deg,#3f9ee0 0%,#8cc8ee 30%,#e9f3f8 48%,#4cc3d4 60%,#9fdcd8 68%,#eee8da 76%,#f2eee6 100%)}
.rate-title{position:absolute;left:15px;top:68px;color:#fff;font-size:12px;font-weight:700}
.rate-sub{position:absolute;left:15px;top:92px;width:118px;font-size:8.2px;line-height:9.5px;font-weight:600;color:var(--ink)}
.rate-note{position:absolute;left:15px;top:209px;width:192px;font-size:7px;line-height:9px;font-weight:600;text-align:justify}

/* exclusive */
.s4 .title{left:18px;top:67px;font-size:12.5px;line-height:15px;text-transform:uppercase}
.excl-lead{position:absolute;left:18px;top:122px;font-size:6.8px;font-weight:700}
.excl-body{position:absolute;left:18px;top:140px;width:174px;font-size:6.8px;line-height:9.2px}

/* own */
.s5 .title{left:16px;top:68px;font-size:12px}
.s5 .bullets{font-size:6.6px}
.s5 .bullets li{line-height:13px}
.own-left{left:16px;top:90px}
.own-right{left:176px;top:90px;width:138px}
.own-right li{line-height:13px!important;text-align:justify}
.own-credit{position:absolute;left:178px;top:221px;color:var(--sky);font-size:11.5px;font-weight:700}

/* welcome */
.s6 .title{left:0;width:100%;text-align:center;top:68px;font-size:11.5px}
.tile{position:absolute;width:90px}
.tile-label{display:block;text-align:center;color:var(--orange);font-size:11px;font-weight:700;line-height:13px}
.tile .photo{position:relative;display:block;width:90px;height:57px;border:2px solid var(--sky)}
.p-hotel{background:linear-gradient(180deg,#e9eef2 0%,#c8b7a0 60%,#6fb1d8 100%)}
.p-cruise{background:linear-gradient(180deg,#a9d3ee 0%,#f1f3f4 55%,#8a8f96 100%)}
.p-weekly{background:linear-gradient(180deg,#6cb7ea 0%,#a8d7f0 55%,#3e8f4d 100%)}
.p-act{background:linear-gradient(180deg,#c7d5df 0%,#f2f2f2 50%,#4b6b84 100%)}
.p-yacht{background:linear-gradient(180deg,#8fc6ea 0%,#e8eef2 50%,#2f7fb4 100%)}
.p-tour{background:linear-gradient(180deg,#6fb6e6 0%,#c9a77c 55%,#7b4d3a 100%)}

/* seen */
.s7 .title{left:0;width:100%;text-align:center;top:50px;font-size:12px}
.feature{position:absolute;top:86px;width:79px}
.feature .icon{display:block;width:55px;height:55px;border-radius:50%;margin:0 auto}
.icon.orange{background:var(--orange)}
.icon.blue{background:var(--sky)}
.feature-label{margin-top:10px;background:var(--grey);color:#fff;font-size:8px;font-weight:700;text-align:center;line-height:15px}
.feature-text{background:#fff;border:1px solid #b8b8b8;height:66px;font-size:6.8px;line-height:10.5px;text-align:center;padding:6px 3px 0;font-weight:600}

/* partners */
.s8 .cover-name{left:28px;top:40px}
.partner{position:absolute;color:#6c6c6c;font-weight:700;white-space:nowrap}
</style>
</head>
<body>

<!-- Cover -->
<section class="slide s1">
  <svg class="cover-sky" viewBox="0 0 345 259" aria-hidden="true">
    <defs>
      <linearGradient id="skyFill" x1="0" y1="0" x2="0" y2="1">
        <stop offset="0" stop-color="#3f86cf"/>
        <stop offset=".55" stop-color="#a9cdee"/>
        <stop offset="1" stop-color="#eef4fa"/>
      </linearGradient>
    </defs>
    <path d="M0 108 C110 70 230 40 345 30 V235 C240 200 120 200 0 232 Z" fill="url(#skyFill)" role="img" aria-label="Airliner flying above clouds"/>
    <path d="M0 100 C110 62 230 34 345 20 V32 C230 44 110 72 0 110 Z" fill="var(--orange)"/>
    <path d="M0 232 C120 200 240 200 345 228 V240 C240 212 120 214 0 244 Z" fill="var(--orange)"/>
  </svg>
  <div class="cover-name"><span class="dot"></span>KVLO EXTRA</div>
  <div class="photo ring photo-pool" style="left:222px;top:22px;width:70px;height:70px" role="img" aria-label="Resort infinity pool beside the sea"></div>
  <ul class="bullets">
    <li>All Destinations</li>
    <li>Every Major Airline</li>
    <li>Best Price at time of Booking</li>
  </ul>
  <div class="url-foot" style="right:24px;top:241px">KVLO.online</div>
</section>

<!-- Who we are -->
<section class="slide s2">
  <svg class="header" viewBox="0 0 346 80" preserveAspectRatio="none" aria-hidden="true">
    <path d="M0 0 H346 V6 C250 18 130 42 0 62 Z" fill="var(--blue)"/>
    <path d="M0 62 C130 42 250 18 346 6 V40 C240 40 120 56 0 72 Z" fill="var(--orange)"/>
  </svg>
  <div class="header-brand">KVLO</div>
  <div class="header-url">KVLO.online</div>
  <h2 class="title">Who We Are</h2>
  <ul class="bullets">
    <li>We are the largest vendor alliance in the world.</li>
    <li>Operating internationally and offered in multiple languages</li>
    <li>Plus 24/7 Real Time Online Booking from anwhere!</li>
    <li>Website with over 250,000 pages "LIVE" ... updated every 20 minutes</li>
    <li>Live staff for Bookings and Support</li>
  </ul>
  <div class="photo ring photo-hut" style="left:23px;top:187px;width:63px;height:63px" role="img" aria-label="Overwater bungalow"></div>
  <div class="photo ring photo-couple" style="left:101px;top:187px;width:63px;height:63px" role="img" aria-label="Couple on holiday"></div>
  <div class="photo ring photo-chairs" style="left:179px;top:187px;width:63px;height:63px" role="img" aria-label="Deck chairs on the beach"></div>
  <div class="photo ring photo-palm" style="left:261px;top:187px;width:63px;height:63px" role="img" aria-label="Palm tree on a tropical beach"></div>
</section>

<!-- Best rate -->
<section class="slide s3">
  <div class="photo beach" role="img" aria-label="Traveller relaxing in a beach chair facing the sea"></div>
  <svg class="header" viewBox="0 0 345 80" preserveAspectRatio="none" aria-hidden="true">
    <path d="M0 0 H345 V6 C250 18 130 42 0 62 Z" fill="var(--blue)"/>
    <path d="M0 62 C130 42 250 18 345 6 V40 C240 40 120 56 0 72 Z" fill="var(--orange)"/>
  </svg>
  <div class="header-brand">KVLO</div>
  <div class="header-url">KVLO.online</div>
  <h2 class="rate-title">Best Rate Guarantee</h2>
  <p class="rate-sub">Kavalo Travel Network Offers a Best Rate Guarantee at Time of Booking</p>
  <p class="rate-note">We Promise to credit you 110% of the price difference if you find cheaper pricing online after you make a reservation through your membership. Simple submit a claim withing 24 hours from booking.</p>
</section>

<!-- Exclusive -->
<section class="slide s4">
  <svg class="header" viewBox="0 0 346 80" preserveAspectRatio="none" aria-hidden="true">
    <path d="M0 0 H346 V6 C250 18 130 42 0 62 Z" fill="var(--blue)"/>
    <path d="M0 62 C130 42 250 18 346 6 V40 C240 40 120 56 0 72 Z" fill="var(--orange)"/>
  </svg>
  <div class="header-brand">KVLO</div>
  <div class="header-url">KVLO.online</div>
  <h2 class="title">Exclusive Travel<br>Rewards for you.</h2>
  <p class="excl-lead">Kavalo Travel Network +EXTRA</p>
  <p class="excl-body">Trip planning today can be challenging. With hundreds of websites, discount sites, hotels and accommodations it can seem overwhelming. Kavalo Travel Network is the exclusive service, offering premium travel opportunities at discounted rates. Book your flight, hotel, excusions and more all in one place.</p>
  <div class="photo ring photo-map" style="left:202px;top:95px;width:132px;height:132px" role="img" aria-label="Hands planning a trip over a map"></div>
</section>

<!-- Why own -->
<section class="slide s5">
  <svg class="header" viewBox="0 0 345 80" preserveAspectRatio="none" aria-hidden="true">
    <path d="M0 0 H345 V6 C250 18 130 42 0 62 Z" fill="var(--blue)"/>
    <path d="M0 62 C130 42 250 18 345 6 V40 C240 40 120 56 0 72 Z" fill="var(--orange)"/>
  </svg>
  <div class="header-brand">KVLO</div>
  <div class="header-url">KVLO.online</div>
  <h2 class="title">Why Would I Own?</h2>
  <ul class="bullets own-left">
    <li>50 Year Membership KVLO</li>
    <li>Pride of Ownership</li>
    <li>Exchange for new places</li>
    <li>Improve your vacation Lifestyle</li>
    <li>Establish Children's lifestyles</li>
    <li>Privacy</li>
  </ul>
  <ul class="bullets own-right">
    <li>Freeze Ownership Cost's of Future Vacations</li>
    <li>Luxury, Fully Furnished Accommodations</li>
    <li>Ownership with deed &amp; Title</li>
    <li>Price Guarantee</li>
    <li>Loan your week to a Friend or Relative</li>
    <li>Guaranteed Opt Out</li>
  </ul>
  <div class="photo ring photo-hut" style="left:23px;top:185px;width:64px;height:64px" role="img" aria-label="Overwater bungalow"></div>
  <div class="photo ring photo-couple" style="left:101px;top:185px;width:64px;height:64px" role="img" aria-label="Couple on holiday"></div>
  <div class="own-credit">Earn Reward Credits</div>
</section>

<!-- Welcome -->
<section class="slide s6">
  <svg class="header" viewBox="0 0 346 80" preserveAspectRatio="none" aria-hidden="true">
    <path d="M0 0 H346 V6 C250 18 130 42 0 62 Z" fill="var(--blue)"/>
    <path d="M0 62 C130 42 250 18 346 6 V40 C240 40 120 56 0 72 Z" fill="var(--orange)"/>
  </svg>
  <div class="header-brand">KVLO</div>
  <div class="header-url">KVLO.online</div>
  <h2 class="title">Welcome to Kavalo Travel Network</h2>
  <div class="tile" style="left:26px;top:92px"><span class="tile-label">Hotels</span><span class="photo p-hotel" role="img" aria-label="Bright hotel room"></span></div>
  <div class="tile" style="left:130px;top:92px"><span class="tile-label">Cruises</span><span class="photo p-cruise" role="img" aria-label="Cruise ship at port"></span></div>
  <div class="tile" style="left:234px;top:92px"><span class="tile-label">Weekly</span><span class="photo p-weekly" role="img" aria-label="Tropical island resort"></span></div>
  <div class="tile" style="left:26px;top:173px"><span class="tile-label">Activities</span><span class="photo p-act" role="img" aria-label="Speedboat on the water"></span></div>
  <div class="tile" style="left:130px;top:173px"><span class="tile-label">Yachts</span><span class="photo p-yacht" role="img" aria-label="Luxury yacht at sea"></span></div>
  <div class="tile" style="left:234px;top:173px"><span class="tile-label">World Tour</span><span class="photo p-tour" role="img" aria-label="Famous world landmarks"></span></div>
</section>

<!-- As seen in -->
<section class="slide s7">
  <svg class="header" viewBox="0 0 345 80" preserveAspectRatio="none" aria-hidden="true">
    <path d="M0 0 H345 V6 C250 18 130 42 0 62 Z" fill="var(--blue)"/>
    <path d="M0 62 C130 42 250 18 345 6 V40 C240 40 120 56 0 72 Z" fill="var(--orange)"/>
  </svg>
  <div class="header-brand">KVLO</div>
  <div class="header-url">KVLO.online</div>
  <h2 class="title">As Seen In:</h2>

  <div class="feature" style="left:11px">
    <svg class="icon orange" viewBox="0 0 55 55" aria-hidden="true">
      <rect x="19" y="12" width="17" height="31" fill="#fff"/>
      <g fill="var(--orange)"><rect x="22" y="16" width="3" height="3"/><rect x="30" y="16" width="3" height="3"/><rect x="22" y="23" width="3" height="3"/><rect x="30" y="23" width="3" height="3"/><rect x="22" y="30" width="3" height="3"/><rect x="30" y="30" width="3" height="3"/><rect x="25" y="37" width="5" height="6"/></g>
    </svg>
    <div class="feature-label">Hotels</div>
    <div class="feature-text">400,000 Hotels and Resorts, with top brands that you trust!</div>
  </div>
  <div class="feature" style="left:93px">
    <svg class="icon blue" viewBox="0 0 55 55" aria-hidden="true">
      <path d="M13 32 L17 23 H37 L41 32 V38 H13 Z" fill="#fff"/>
      <circle cx="19" cy="38" r="3.5" fill="var(--sky)" stroke="#fff" stroke-width="2"/>
      <circle cx="35" cy="38" r="3.5" fill="var(--sky)" stroke="#fff" stroke-width="2"/>
      <rect x="20" y="25" width="14" height="6" fill="var(--sky)"/>
    </svg>
    <div class="feature-label">Car Rentals</div>
    <div class="feature-text">8,000 nationwide locations. Includes comparative pricing!</div>
  </div>
  <div class="feature" style="left:175px">
    <svg class="icon orange" viewBox="0 0 55 55" aria-hidden="true">
      <path d="M22 20 V16 H33 V20" fill="none" stroke="#fff" stroke-width="2.5"/>
      <rect x="16" y="20" width="23" height="19" rx="3" fill="#fff"/>
    </svg>
    <div class="feature-label">Weekly Stays</div>
    <div class="feature-text">8 day and night resort stays in destinations around the world.</div>
  </div>
  <div class="feature" style="left:258px">
    <svg class="icon blue" viewBox="0 0 55 55" aria-hidden="true">
      <path d="M12 33 C20 38 35 38 43 33 C35 35 20 35 12 33 Z" fill="#fff" stroke="#fff" stroke-width="2"/>
      <circle cx="27" cy="22" r="3" fill="#fff"/>
      <path d="M27 25 V32" stroke="#fff" stroke-width="3"/>
      <path d="M17 17 L38 36" stroke="#fff" stroke-width="2"/>
    </svg>
    <div class="feature-label">Activities</div>
    <div class="feature-text">Thousand of activities and excursions to add to your vacation.</div>
  </div>
</section>

<!-- Partners -->
<section class="slide s8">
  <svg class="cover-sky" viewBox="0 0 346 259" aria-hidden="true">
    <path d="M0 110 C110 80 230 50 346 30 V38 C230 58 110 88 0 120 Z" fill="var(--orange)"/>
    <path d="M0 120 C110 88 230 58 346 38 V210 C230 196 110 200 0 220 Z" fill="#fff"/>
    <path d="M0 220 C110 200 230 196 346 210 V222 C230 210 110 212 0 232 Z" fill="var(--orange)"/>
  </svg>
  <div class="cover-name"><span class="dot"></span>KVLO EXTRA</div>
  <span class="partner" style="right:14px;top:86px;font-size:14px">Nordair</span>
  <span class="partner" style="right:14px;top:112px;font-size:9px">Skyline West</span>
  <span class="partner" style="left:140px;top:128px;font-size:9px">Island Pacific Air</span>
  <span class="partner" style="right:14px;top:136px;font-size:9px">Straits Air</span>
  <span class="partner" style="left:14px;top:152px;font-size:10px">Desert Star</span>
  <span class="partner" style="left:72px;top:144px;font-size:7.5px">Crown Airways</span>
  <span class="partner" style="left:62px;top:170px;font-size:10px;letter-spacing:2px">MERIDIAN</span>
  <span class="partner" style="left:142px;top:172px;font-size:7px">Lotus Air</span>
  <span class="partner" style="left:190px;top:162px;font-size:7.5px">Aloha Wings</span>
  <span class="partner" style="right:14px;top:170px;font-size:10px;letter-spacing:1px">MAPLE AIR</span>
  <span class="partner" style="left:128px;top:196px;font-size:9px">Southern Cross</span>
  <span class="partner" style="right:14px;top:196px;font-size:10px">Liberty Airlines</span>
  <div class="url-foot" style="right:24px;top:242px">KVLO.online</div>
</section>

</body>
</html>
```